Business Card design for an International Import Export House

We need a Business Card design for our import export business. We trade in Minerals, Metals, Rice, Sugar, Steel etc.. The design should be minimalistic. It may or may not contain the physical address. In case you want to include the physical address - 418 Verandah Heights, Marlow Sector 9, Gurgaon, Haryana, India, 122009.

Target Market(s)

Steel Mills or Steel Plants, Factories, Mining businesses, Industrial houses, Government Agencies

Industry/Entity Type

Importer

Contact Information for Business Card

Business Name - Tessan Overseas

Font styles to use
Other font styles liked:
• montserrat

Requirements
Must have
• Ravi Kandola - President
• www.tessanoverseas.com
• ravi@tessanoverseas.com
• +91-987-654-3217
Nice to have
• worldwide suppliers of ores

```html
<!DOCTYPE html>
<html lang="en">
<head>
<meta charset="utf-8">
<title>Tessan Overseas — Business Card</title>
<link rel="stylesheet" href="https://fonts.googleapis.com/css2?family=Montserrat:wght@600;700&family=Questrial&display=swap">
<style>
  :root {
    --backdrop: #13222a;
    --card: #ffffff;
    --ink: #1d262d;
    --ink-soft: #3a444b;
    --brand: #3a91b3;
    --brand-pale: #d6e6ee;
  }
  * { box-sizing: border-box; margin: 0; padding: 0; }
  html, body {
    width: 1200px; height: 720px; overflow: hidden;
    background: var(--backdrop);
  }
  .stage {
    position: relative; width: 1200px; height: 720px;
    display: flex; align-items: center; justify-content: center; gap: 40px;
  }
  .card {
    position: relative; width: 540px; height: 309px;
    background: var(--card);
    box-shadow: 0 14px 34px rgba(0,0,0,.45);
    font-family: "Questrial", "Century Gothic", sans-serif;
    color: var(--ink);
  }
  .brand {
    font-family: "Montserrat", sans-serif; font-weight: 700;
    color: var(--brand); letter-spacing: -0.5px; text-transform: uppercase;
    display: flex; align-items: center; gap: 8px; white-space: nowrap;
  }
  .brand-dot {
    width: 12px; height: 12px; border-radius: 50%; background: var(--brand);
  }
  .rule {
    height: 3px; border-radius: 2px;
    background: linear-gradient(90deg, var(--brand-pale), var(--brand));
  }

  /* Front: person and contact */
  .card-front .brand { position: absolute; left: 58px; top: 140px; font-size: 22px; }
  .person { position: absolute; right: 68px; top: 52px; text-align: center; }
  .person-name { font-size: 23px; font-weight: 700; letter-spacing: .3px; }
  .person-title { font-size: 15px; color: var(--ink-soft); margin-top: 4px; }
  .card-front .rule { width: 210px; margin-top: 6px; }
  .contact-list {
    position: absolute; left: 300px; top: 210px; list-style: none;
    font-size: 15px; line-height: 22px;
  }
  .contact-list li { display: flex; align-items: center; gap: 8px; }
  .contact-icon { width: 13px; height: 13px; flex: none; }
  .contact-web { color: var(--brand); }

  /* Back: brand and tagline */
  .card-back .lockup { position: absolute; left: 190px; top: 112px; }
  .card-back .brand { font-size: 25px; }
  .tagline {
    font-size: 13px; letter-spacing: 2.6px; text-transform: uppercase;
    color: var(--ink-soft); margin-top: 10px;
  }
  .card-back .rule { width: 282px; margin-top: 12px; }
</style>
</head>
<body>
<main class="stage">
  <section class="card card-front" aria-label="Card front">
    <div class="brand"><span class="brand-dot"></span>Tessan Overseas</div>
    <div class="person">
      <p class="person-name">Ravi Kandola</p>
      <p class="person-title">President</p>
      <div class="rule"></div>
    </div>
    <ul class="contact-list">
      <li>
        <svg class="contact-icon" viewBox="0 0 16 16" aria-hidden="true"><circle cx="8" cy="8" r="8" fill="#1d262d"/><path d="M5 4.2l1.6-.3.8 2-1 .8a6 6 0 0 0 2.9 2.9l.8-1 2 .8-.3 1.6c-3.6.3-7.1-3.2-6.8-6.8z" fill="#fff"/></svg>
        +91-987-654-3217
      </li>
      <li>
        <svg class="contact-icon" viewBox="0 0 16 16" aria-hidden="true"><circle cx="8" cy="8" r="8" fill="#1d262d"/><rect x="4" y="5" width="8" height="6" fill="none" stroke="#fff" stroke-width="1.2"/><path d="M4 5l4 3.3L12 5" fill="none" stroke="#fff" stroke-width="1.2"/></svg>
        ravi@tessanoverseas.com
      </li>
      <li class="contact-web">
        <svg class="contact-icon" viewBox="0 0 16 16" aria-hidden="true"><circle cx="8" cy="8" r="8" fill="#3a91b3"/><circle cx="8" cy="8" r="4.5" fill="none" stroke="#fff" stroke-width="1.1"/><path d="M3.5 8h9M8 3.5c-2 2.5-2 6.5 0 9M8 3.5c2 2.5 2 6.5 0 9" fill="none" stroke="#fff" stroke-width="1"/></svg>
        www.tessanoverseas.com
      </li>
    </ul>
  </section>

  <section class="card card-back" aria-label="Card back">
    <div class="lockup">
      <div class="brand">Tessan Overseas</div>
      <p class="tagline">Worldwide suppliers of ores</p>
      <div class="rule"></div>
    </div>
  </section>
</main>
</body>
</html>
```